Dane Moro films- wedding and event films company website. DESKTOP AND MOBILE

We need a website for a high-end wedding and event film production company. Looking for a very modern and elegant design. my old website is www.danemorofilms.example

I like the "white/black/rose gold" color scheme of my logo.

really looking for a sleek modern design the breaths professional and artistic.

Target Market(s)

wedding and event films.

Industry/Entity Type

Film Production

Number of Pages Required

5+ page

Colors

Designer to choose colors to be used in the design.

Requirements
Must have
• website name will be www.danemorofilms.example
• tagline is "CINEMATIC STORIES ABOUT YOU"
• sections: HOME, CONTACT, ABOUT, FILMS, BLOG
• You can see my old website at danemorofilms.example
• Website about section:
• Dane Moro Films was Established with the basis of truly cinematic and artistic films in mind. Dane and his team routinely travel the globe documenting weddings and events for high profile clients and discerning couples. Dane was born and raised in Maui Hawaii and has a unique approach to his films that embody the essence of a Hollywood film. Dane has spent the last 10 years traveling the world documenting corporate events and weddings with multiple Award winning production companies. In 2017 Dane decided to establish his own brand “Dane Moro films” that will take everything he has learned with his past experiences and push it to the next level. Aside from his personal achievements, Dane is extremely passionate about his craft and always looks forward to handcrafting beautiful wedding/event films for his clients. The style of work is non-traditional and the day of filming is extremely unobtrusive (as we are looking for natural-candid/ raw emotions).
• If you are looking for the best price in town, we are probably not the best option, but if you’re looking for the best quality and peace of mind on your wedding day, then you’re in the right place. Dane Moro Films is a boutique studio that only accepts a limited number of assignments per year. Inquire early to ensure availability.
• LINKS TO VIMEO VIDEOS THAT WILL BE IN THE "FILMS' SECTION.
• BRENT FILM TRAILER - https://clipvault.example/418205736
• BRENT FEATURE FILM - https://clipvault.example/527910384
• NORA AND PAUL'S WEDDING - https://clipvault.example/649382015
• DRONE DEMO REEL - https://clipvault.example/751046923
• WEDDING INDUSTRY EVENT PARTY - https://clipvault.example/862937104/7a2d9c3e8b
• images that you can use on site are here: https://maribelortegaphotos.picvault.example/gallery/ruth&glen/
• password is: meadow

```html
<!DOCTYPE html>
<html lang="en">
<head>
<meta charset="utf-8">
<title>Dane Moro Films</title>
<link rel="stylesheet" href="https://fonts.googleapis.com/css2?family=Poppins:wght@300;400;500;600;700&display=swap">
<style>
:root{
  --accent:#ec8a2c;
  --ink:#2b2b2b;
  --muted:#555;
  --white:#fff;
  --brown:#5b3412;
  --brown-dark:#43250b;
}
*{box-sizing:border-box;margin:0;padding:0}
html,body{width:1200px;height:3253px;overflow:hidden;background:#fff}
body{font-family:'Poppins',sans-serif;color:var(--ink);position:relative}
.abs{position:absolute}
.outline-btn{position:absolute;border:1.5px solid var(--accent);color:var(--accent);font-size:12px;display:flex;align-items:center;justify-content:center;gap:8px;text-decoration:none;letter-spacing:.3px}

/* hero */
.hero{position:absolute;left:0;top:0;width:1200px;height:667px;
  background:radial-gradient(ellipse 70% 80% at 52% 40%,#c9c9c9 0%,#a2a2a2 30%,#777 60%,#4a4a4a 100%)}
.hero-shade{position:absolute;inset:0;background:linear-gradient(180deg,rgba(0,0,0,.35),rgba(0,0,0,0) 35%,rgba(0,0,0,.1) 70%,rgba(0,0,0,.35))}
.brand{position:absolute;left:162px;top:88px;display:flex;align-items:center;gap:10px;color:var(--white);font-size:16px;font-weight:400;letter-spacing:1px}
.brand-mark{width:16px;height:16px;background:var(--accent)}
.topbar{position:absolute;left:494px;top:40px;display:flex;align-items:center;gap:14px;color:var(--white);font-size:11px;font-weight:600}
.topbar .dot{width:9px;height:9px;border:1.5px solid var(--white);border-radius:50%}
.topbar .dot.acc{border-color:var(--accent);background:var(--accent)}
.nav{position:absolute;left:412px;top:82px;width:376px;height:28px;border-bottom:1.5px solid rgba(255,255,255,.85);display:flex;justify-content:space-around;align-items:center;font-size:12px;color:var(--white)}
.nav .active{color:var(--accent)}
.hero-title{position:absolute;left:0;width:1200px;top:432px;text-align:center;color:var(--white);font-size:36px;font-weight:300}
.hero-quote{position:absolute;left:0;width:1200px;top:498px;text-align:center;color:var(--white);font-size:12px;line-height:23px}
.hero-btn{left:536px;top:563px;width:128px;height:32px}
.hero-arrow{position:absolute;top:316px}

/* about */
.about-photo{left:174px;top:742px;width:366px;height:366px;background:radial-gradient(ellipse 55% 60% at 50% 40%,#8a8a8a,#3e3e3e 60%,#d8d8d8 100%)}
.about-rule{left:575px;top:826px;width:1px;height:182px;background:#bbb}
.about-title{left:628px;top:764px;font-size:28px;font-weight:300;color:var(--ink)}
.about-text{left:628px;top:826px;width:388px;font-size:12.3px;line-height:28px;color:var(--muted);letter-spacing:.2px}
.about-btn{left:628px;top:1056px;width:138px;height:42px;font-weight:500}

/* films grid */
.films{position:absolute;left:0;top:1190px;width:1200px;height:592px;display:grid;grid-template-columns:400px 400px 400px;grid-template-rows:296px 296px}
.film{border:1px solid #2e2e2e}
.film.t1{background:radial-gradient(ellipse at 60% 55%,#9b9b9b,#4b4b4b 70%)}
.film.t3{background:radial-gradient(ellipse at 70% 50%,#7e7e7e,#565656 50%,#3a3a3a)}
.film.t4{background:radial-gradient(ellipse at 45% 50%,#8c8c8c,#3d3d3d 75%)}
.film.t5{background:radial-gradient(ellipse at 50% 60%,#a4a4a4,#5a5a5a 70%)}
.film.t6{background:radial-gradient(ellipse at 40% 55%,#999,#474747 75%)}
.film.featured{background:radial-gradient(ellipse at 55% 50%,#8e9c6a,#55733e 55%,#2f4524);border:6px solid var(--accent)}
.films-btn{left:528px;top:1815px;width:144px;height:38px}

/* blog */
.blog-heading{left:0;width:1200px;top:1944px;text-align:center;font-size:30px;font-weight:400}
.post-img-lg{left:160px;top:2027px;width:426px;height:223px;background:radial-gradient(ellipse at 55% 40%,#a7b48a,#5f7d45 55%,#34502a)}
.post-img-sm{width:113px;height:154px;border:3px solid var(--accent);background:radial-gradient(ellipse at 50% 70%,#2d3f5c,#3d5a2e 75%)}
.meta{font-size:10px;font-weight:700;color:var(--ink)}
.meta span{color:var(--accent)}
.post-title{font-weight:700;font-size:17px;line-height:27px;color:var(--ink)}
.post-title.sm{font-size:14px;line-height:22px}
.excerpt{font-size:11.5px;line-height:21px;color:var(--muted)}
.blog-btn{left:610px;top:2428px;width:168px;height:40px}

/* contact */
.contact{position:absolute;left:0;top:2575px;width:1200px;height:678px;background:radial-gradient(ellipse at 50% 40%,#6b4018,var(--brown) 50%,var(--brown-dark))}
.contact-title{left:0;width:1200px;top:60px;text-align:center;font-size:34px;font-weight:700;color:var(--white)}
.contact-underline{left:553px;top:108px;width:94px;height:4px;background:var(--accent)}
.contact-sub{left:0;width:1200px;top:122px;text-align:center;font-size:22px;font-weight:300;color:var(--white)}
.field{position:absolute;border:1.5px solid rgba(255,255,255,.85);color:var(--white);font-size:13px;padding:9px 12px}
.submit{left:258px;top:432px;width:142px;height:50px;background:var(--accent);color:var(--white);font-size:16px;display:flex;align-items:center;justify-content:center;gap:12px}
.info{left:768px;color:var(--white)}
.info-text{top:210px;font-size:14px;line-height:27px;width:220px}
.info-row{display:flex;align-items:center;gap:16px;left:730px}
.phone{top:288px;font-size:22px;font-weight:600}
.email{top:330px;font-size:14px}
.travel{top:362px;font-size:14px;line-height:27px;width:220px}
.footer-rule{left:122px;top:562px;width:956px;height:1.5px;background:rgba(255,255,255,.55)}
.copyright{left:0;width:1200px;top:586px;text-align:center;font-size:13px;color:var(--white)}
</style>
</head>
<body>

<section class="hero" role="img" aria-label="Black and white photo of a bride and groom walking through wedding guests">
  <div class="hero-shade"></div>
</section>
<div class="brand"><span class="brand-mark"></span>DANE MORO FILMS</div>
<div class="topbar"><span class="dot"></span><span class="dot"></span><span class="dot acc"></span><span>Call us: 808-555-0143</span></div>
<nav class="nav"><span class="active">HOME</span><span>CONTACT</span><span>ABOUT</span><span>FILMS</span><span>BLOG</span></nav>
<svg class="hero-arrow" style="left:28px" width="14" height="20" viewBox="0 0 14 20"><path d="M10 3 3 10l7 7" stroke="#fff" stroke-width="2" fill="none"/></svg>
<svg class="hero-arrow" style="left:1160px" width="14" height="20" viewBox="0 0 14 20"><path d="M4 3l7 7-7 7" stroke="#fff" stroke-width="2" fill="none"/></svg>
<svg class="abs" style="left:1152px;top:356px" width="28" height="28" viewBox="0 0 28 28"><circle cx="14" cy="14" r="12" stroke="#fff" stroke-width="1.5" fill="none"/><path d="M10 18l8-8M14 10h4v4M10 14v4h4" stroke="#fff" stroke-width="1.3" fill="none"/></svg>
<svg class="abs" style="left:1160px;top:398px" width="12" height="14" viewBox="0 0 12 14"><path d="M2 2l8 5-8 5z" stroke="#fff" stroke-width="1.3" fill="none"/></svg>
<h1 class="hero-title">Cinematic Stories About You</h1>
<p class="hero-quote">"Dane really is one of the best film makers in<br>Hawaii, great work Dane! We loved the film!" — Lena Vask</p>
<a class="outline-btn hero-btn">CONTACT US</a>

<div class="abs about-photo" role="img" aria-label="Black and white portrait of the filmmaker"></div>
<div class="abs about-rule"></div>
<h2 class="abs about-title">About Dane Moro Films</h2>
<p class="abs about-text">Dane Moro Films was Established with the basis of truly cinematic and artistic films in mind. Dane and his team routinely travel the globe documenting weddings and events for high profile clients and discerning couples. Dane was born and raised in Maui Hawaii and has a unique approach to his films that embody the essence of a Hollywood film.</p>
<a class="outline-btn about-btn">READ MORE <svg width="7" height="10" viewBox="0 0 7 10"><path d="M1 1l4 4-4 4" stroke="#ec8a2c" stroke-width="1.6" fill="none"/></svg></a>

<section class="films">
  <div class="film t1" role="img" aria-label="Black and white film still of a couple dancing at a reception"></div>
  <div class="film featured" role="img" aria-label="Film still of a bride in a garden"></div>
  <div class="film t3" role="img" aria-label="Black and white film still of a smiling wedding guest"></div>
  <div class="film t4" role="img" aria-label="Black and white film still of a couple posing together"></div>
  <div class="film t5" role="img" aria-label="Black and white film still of children playing at a wedding"></div>
  <div class="film t6" role="img" aria-label="Black and white film still of an older couple at a party"></div>
</section>
<a class="outline-btn films-btn">VIEW ALL VIDEOS</a>

<h2 class="abs blog-heading">Our Latest Blogs</h2>
<div class="abs post-img-lg" role="img" aria-label="Groom lifting bride outdoors"></div>
<p class="abs meta" style="left:160px;top:2262px">◷ BY <span>DANE MORO &nbsp;OCTOBER 30, 2017</span>, 11:03AM</p>
<h3 class="abs post-title" style="left:160px;top:2280px;width:430px">Lorem ipsum dolor sit amet, consectetur adipiscing elit donec pulvinar</h3>
<p class="abs excerpt" style="left:160px;top:2340px;width:430px">mentum et tempor ullamcorper, facilisis vitae leo. Integer tempor nunc felis. Nam pharetra risus in laoreet venenatis...</p>

<div class="abs post-img-sm" style="left:614px;top:2025px" role="img" aria-label="Groom in a navy suit"></div>
<p class="abs meta" style="left:778px;top:2022px">◷ BY <span>DANE MORO &nbsp;September 12, 2017</span>, 10:20AM</p>
<h3 class="abs post-title sm" style="left:778px;top:2042px;width:270px">Lorem ipsum dolor sit amet, consectetur adipiscing elit don</h3>
<p class="abs excerpt" style="left:778px;top:2094px;width:265px">Sed purus neque, maximus vitae nulla vel, volutpat pulvinar est. Vivamus eu ante non quam porttitor fermentum vitae eu quam...</p>

<div class="abs post-img-sm" style="left:614px;top:2230px" role="img" aria-label="Groom with a young boy"></div>
<p class="abs meta" style="left:778px;top:2227px">◷ BY <span>DANE MORO &nbsp;August 28, 2017</span>, 09:20AM</p>
<h3 class="abs post-title sm" style="left:778px;top:2247px;width:270px">Lorem ipsum dolor sit amet, consectetur adipiscing elit don</h3>
<p class="abs excerpt" style="left:778px;top:2299px;width:265px">Sed purus neque, maximus vitae nulla vel, volutpat pulvinar est. Vivamus eu ante non quam porttitor fermentum vitae eu quam...</p>
<a class="outline-btn blog-btn">Read All Blog Posts <svg width="7" height="10" viewBox="0 0 7 10"><path d="M1 1l4 4-4 4" stroke="#ec8a2c" stroke-width="1.6" fill="none"/></svg></a>

<section class="contact" role="img" aria-label="Warm brown tinted photo of a wedding celebration">
  <h2 class="abs contact-title">CONTACT</h2>
  <div class="abs contact-underline"></div>
  <p class="abs contact-sub">Write and visit us</p>
  <div class="field" style="left:258px;top:197px;width:210px;height:38px">Name</div>
  <div class="field" style="left:480px;top:197px;width:210px;height:38px">Email</div>
  <div class="field" style="left:258px;top:247px;width:210px;height:38px">Phone No.</div>
  <div class="field" style="left:480px;top:247px;width:210px;height:38px">Subject</div>
  <div class="field" style="left:258px;top:300px;width:432px;height:118px">Message</div>
  <div class="abs submit">Submit <svg width="20" height="16" viewBox="0 0 20 16"><path d="M1 7 19 1 13 15 10 9z" fill="#fff"/></svg></div>
  <p class="abs info info-text">For pricing and availability please contact Dane:</p>
  <div class="abs info info-row phone"><svg width="22" height="22" viewBox="0 0 22 22"><path d="M5 2l4 4-2 3c1 3 3 5 6 6l3-2 4 4-3 3C9 20 2 13 2 5z" stroke="#fff" stroke-width="1.3" fill="none"/></svg>808-555-0143</div>
  <div class="abs info info-row email"><svg width="20" height="14" viewBox="0 0 20 14"><rect x="1" y="1" width="18" height="12" stroke="#fff" fill="none" stroke-width="1.3"/><path d="M1 1l9 7 9-7" stroke="#fff" fill="none" stroke-width="1.3"/></svg>dane@danemorofilms.example</div>
  <p class="abs info travel">We are available to travel anywhere!</p>
  <div class="abs footer-rule"></div>
  <p class="abs copyright">© Copyright 2017. Dane Moro Films. All rights reserved.</p>
</section>

</body>
</html>
```